new roofing company card

New primary business card for roofing company.

Industry/Entity Type

Residential roofing/Specializing in Asphalt and Standing seam metal roofing

Contact Information for Business Card

Phone number is: 484 672 1058 Email: support@fennridgeroofworks.com website: www.fennridgeroofworks.com

Colors
EB3D1F
EC4F4E
F09395
F8D3D4
FCEDEE

```html
<!DOCTYPE html>
<html lang="en">
<head>
<meta charset="utf-8">
<title>Fennridge Roofworks — Business Card</title>
<link href="https://fonts.googleapis.com/css2?family=Lato:wght@400;700;900&display=swap" rel="stylesheet">
<style>
  :root {
    --stage: #1c1c1c;
    --card-dark: #2b2c2b;
    --card-light: #ffffff;
    --red: #eb3d1f;
    --red-deep: #c8352a;
    --ink: #2b2c2b;
    --silver: #c9c9c9;
    --white: #ffffff;
  }
  * { box-sizing: border-box; margin: 0; padding: 0; }
  html, body {
    width: 1200px; height: 977px; overflow: hidden;
    background: var(--stage);
    font-family: "Lato", sans-serif;
  }
  .canvas { position: relative; width: 1200px; height: 977px; }
  .card {
    position: absolute; width: 540px; height: 310px;
    border-radius: 18px; overflow: hidden;
    box-shadow: 0 10px 30px rgba(0,0,0,.45);
  }
  .card--front { left: 40px; top: 333px; background: var(--card-dark); }
  .card--back  { left: 620px; top: 333px; background: var(--card-light); }

  .brand {
    position: absolute; display: flex; align-items: center; gap: 10px;
    font-weight: 900; letter-spacing: 1px; text-transform: uppercase;
    line-height: 1.05;
  }
  .brand__mark { width: 14px; height: 14px; flex: none; background: var(--red); }
  .card--front .brand {
    left: 0; right: 0; top: 0; bottom: 0; justify-content: center;
    color: var(--silver); font-size: 30px;
  }
  .card--back .brand {
    right: 38px; top: 48px; color: var(--ink); font-size: 24px; text-align: right;
  }

  .back-shapes { position: absolute; inset: 0; }
  .band { fill: var(--red-deep); }
  .base { fill: var(--card-dark); }

  .person {
    position: absolute; left: 150px; top: 182px; color: var(--white);
  }
  .person__name {
    color: var(--red); font-weight: 900; font-size: 22px; letter-spacing: .5px;
    text-transform: uppercase; line-height: 26px;
  }
  .person__role { font-size: 13px; line-height: 16px; margin-top: 1px; }
  .contacts { list-style: none; margin-top: 10px; }
  .contacts li {
    display: flex; align-items: center; gap: 8px;
    font-size: 12.5px; line-height: 19px;
  }
  .contacts svg { width: 12px; height: 12px; flex: none; }
  .icon-bg { fill: var(--red); }
  .icon-fg { fill: none; stroke: var(--white); stroke-width: 1.4; stroke-linecap: round; stroke-linejoin: round; }
</style>
</head>
<body>
<main class="canvas">
  <section class="card card--front" aria-label="Card front">
    <div class="brand"><span class="brand__mark"></span><span>Fennridge<br>Roofworks</span></div>
  </section>

  <section class="card card--back" aria-label="Card back">
    <svg class="back-shapes" viewBox="0 0 540 310" preserveAspectRatio="none">
      <polygon class="band" points="0,282 92,116 540,104 540,138 122,162 42,310 0,310"/>
      <polygon class="base" points="58,310 132,174 540,150 540,310"/>
    </svg>

    <div class="brand"><span class="brand__mark"></span><span>Fennridge<br>Roofworks</span></div>

    <div class="person">
      <p class="person__name">Daniel Hartwell</p>
      <p class="person__role">Founder &amp; CEO</p>
      <ul class="contacts">
        <li>
          <svg viewBox="0 0 12 12"><rect class="icon-bg" width="12" height="12" rx="3"/><path class="icon-fg" d="M4 3l1 2-1 1q1 2 2 2l1-1 2 1-1 1.5q-4 0-5.5-5.5z"/></svg>
          484 672 1058
        </li>
        <li>
          <svg viewBox="0 0 12 12"><rect class="icon-bg" width="12" height="12" rx="3"/><path class="icon-fg" d="M3 4h6v4H3zM3 4l3 2.2L9 4"/></svg>
          support@fennridgeroofworks.com
        </li>
        <li>
          <svg viewBox="0 0 12 12"><rect class="icon-bg" width="12" height="12" rx="3"/><circle class="icon-fg" cx="6" cy="6" r="3"/><path class="icon-fg" d="M3 6h6M6 3q-1.5 3 0 6M6 3q1.5 3 0 6"/></svg>
          www.fennridgeroofworks.com
        </li>
      </ul>
    </div>
  </section>
</main>
</body>
</html>
```